Computer tuition business needs Business card and Advertising Flyer

I am starting up a new business "Dorian Featherby Computer Services" (DFCS for short) based in the Manning Valley NSW Australia.
The primary focus is on tuition\advice to the elderly and less computer literate in the region.
I will not be providing any repair services.

I have the line "At your home, On your computer, Answering your questions" in my head

I will need a Business card design (one sided) and Advertising Flyer design (A4 size, grayscale ).

Contact details on all these are - Mobile: 0412-683-904
- Email : dfeatherby.techhelp@examplemail.net

Target Market(s)

The primary focus is on tuition\advice to the elderly and less computer literate in the Manning Valley region of

Industry/Entity Type

Computer

```html
<!DOCTYPE html>
<html lang="en">
<head>
<meta charset="utf-8">
<title>Dorian Featherby Computer Services – Business Card</title>
<link rel="stylesheet" href="https://fonts.googleapis.com/css2?family=Open+Sans:wght@400;700&display=swap">
<style>
  :root {
    --backdrop: #e8e6e2;
    --card: #ffffff;
    --ink: #231f20;
    --accent-soft: rgba(244, 150, 122, 0.55);
    --accent-fade: rgba(244, 150, 122, 0);
    --band-blue: #2e3192;
    --band-text: #ffffff;
  }
  * { margin: 0; padding: 0; box-sizing: border-box; }
  html, body {
    width: 1200px;
    height: 750px;
    overflow: hidden;
    background: var(--backdrop);
    font-family: "Open Sans", Arial, sans-serif;
  }
  .business-card {
    position: absolute;
    left: 75px;
    top: 28px;
    width: 1050px;
    height: 694px;
    background: var(--card);
    overflow: hidden;
    box-shadow: 0 6px 24px rgba(0,0,0,0.12);
  }
  .accent-glow {
    position: absolute;
    left: 415px;
    top: 70px;
    width: 220px;
    height: 320px;
    border-radius: 50%;
    background: radial-gradient(ellipse at center, var(--accent-soft) 0%, var(--accent-fade) 72%);
  }
  .tagline {
    position: absolute;
    left: 0;
    width: 100%;
    top: 86px;
    text-align: center;
    font-weight: 700;
    font-size: 66px;
    line-height: 81px;
    letter-spacing: 1px;
    color: var(--ink);
    text-transform: uppercase;
  }
  .company-name {
    position: absolute;
    left: 0;
    width: 100%;
    top: 386px;
    text-align: center;
    font-weight: 700;
    font-size: 37px;
    line-height: 44px;
    letter-spacing: 0.5px;
    color: var(--ink);
    text-transform: uppercase;
  }
  .phone-band {
    position: absolute;
    left: 0;
    top: 453px;
    width: 100%;
    height: 117px;
    background: var(--band-blue);
    display: flex;
    align-items: center;
    justify-content: center;
    gap: 18px;
    color: var(--band-text);
  }
  .phone-band .phone-icon { width: 52px; height: 60px; fill: var(--band-text); }
  .phone-number {
    font-weight: 700;
    font-size: 80px;
    line-height: 1;
    letter-spacing: 1px;
  }
  .email-line {
    position: absolute;
    left: 0;
    top: 594px;
    width: 100%;
    height: 44px;
    display: flex;
    align-items: center;
    justify-content: center;
    gap: 14px;
    color: var(--ink);
  }
  .email-line .mail-icon { width: 36px; height: 26px; }
  .email-address {
    font-weight: 400;
    font-size: 28px;
    line-height: 1;
  }
</style>
</head>
<body>
  <main class="business-card">
    <div class="accent-glow" role="img" aria-label="Large soft orange decorative motif behind the headline"></div>
    <h1 class="tagline">At your home, on your<br>computer, answering<br>your questions</h1>
    <p class="company-name">Dorian Featherby Computer Services</p>
    <div class="phone-band">
      <svg class="phone-icon" viewBox="0 0 24 28" aria-hidden="true">
        <path d="M6.2 1.5c.6-.4 1.4-.2 1.8.4l2.6 4.6c.3.6.2 1.3-.3 1.7L8.5 9.6c-.4.3-.5.8-.3 1.3 1.2 2.8 2.8 5.6 4.8 8 .3.4.9.5 1.3.3l2-1.1c.6-.3 1.3-.2 1.7.4l3 4.3c.4.6.3 1.4-.3 1.8l-2 1.5c-1 .7-2.3.9-3.4.4C9.6 23.8 4.7 16.4 3.2 7.9 3 6.7 3.4 5.5 4.3 4.7z"/>
        <path d="M13 3.5a8 8 0 0 1 7 7" fill="none" stroke="#fff" stroke-width="1.6" stroke-linecap="round"/>
        <path d="M12.6 7a4.5 4.5 0 0 1 4 4" fill="none" stroke="#fff" stroke-width="1.6" stroke-linecap="round"/>
      </svg>
      <span class="phone-number">0412-683-904</span>
    </div>
    <div class="email-line">
      <svg class="mail-icon" viewBox="0 0 38 28" aria-hidden="true">
        <rect x="1.5" y="1.5" width="35" height="25" fill="none" stroke="var(--ink)" stroke-width="2.4"/>
        <path d="M1.5 1.5 19 16 36.5 1.5M1.5 26.5 14 12M36.5 26.5 24 12" fill="none" stroke="var(--ink)" stroke-width="2.4"/>
      </svg>
      <span class="email-address">dfeatherby.techhelp@examplemail.net</span>
    </div>
  </main>
</body>
</html>
```